Steadfast MD - Sleep Medicine Specialist - Business Cards

We are a new medical practice called Steadfast MD. We are sleep medicine specialists and we will be conducting sleep studies on patients with sleep related ailments. We want the business card to be bold, professional, and clean with the logo as the stand out visual piece. We dont like wild flashy designs. We want our design to be bold and classic while at the same time conveying who we are and what we do. We are reliable, professional, and the best in the business.

Industry/Entity Type

Health Care

Contact Information for Business Card

- Clean
- Bold
- Classic
- not cluttered

Requirements
Must have
• logo, website, phone number
Nice to have
• several options to choose from
Should not have
• flashy imaged - reflective print - images of people sleeping

```html
<!DOCTYPE html>
<html lang="en">
<head>
<meta charset="utf-8">
<title>Steadfast MD – Business Cards</title>
<link rel="stylesheet" href="https://fonts.googleapis.com/css2?family=Inter:wght@400;600;700&display=swap">
<style>
  :root {
    --backdrop: #d8d8d8;
    --card-light: #ffffff;
    --card-dark: #000000;
    --brand-red: #e3231b;
    --ink: #111111;
    --ink-soft: #222222;
    --tint-light: #f8e1da;
    --tint-dark: #2b2422;
  }
  * { margin: 0; padding: 0; box-sizing: border-box; }
  html, body {
    width: 1200px;
    height: 800px;
    overflow: hidden;
    background: var(--backdrop);
    font-family: "Inter", Arial, sans-serif;
  }
  .sheet { position: relative; width: 1200px; height: 800px; }

  .card {
    position: absolute;
    top: 283px;
    width: 429px;
    height: 238px;
    overflow: hidden;
  }
  .card--front { left: 111px; background: var(--card-light); }
  .card--back  { left: 638px; background: var(--card-dark); }

  .card__ring {
    position: absolute;
    border-radius: 50%;
    border-style: solid;
  }
  .card--front .card__ring {
    left: 277px; top: -10px;
    width: 156px; height: 156px;
    border-width: 4px;
    border-color: var(--tint-light);
  }
  .card--back .card__ring {
    left: 240px; top: -33px;
    width: 212px; height: 212px;
    border-width: 5px;
    border-color: var(--tint-dark);
  }

  .brand {
    position: absolute;
    display: flex;
    align-items: center;
    gap: 8px;
  }
  .brand__dot {
    width: 50px; height: 50px;
    border-radius: 50%;
    border: 3px solid var(--brand-red);
  }
  .brand__name {
    font-weight: 700;
    font-size: 23px;
    letter-spacing: -0.5px;
  }
  .card--front .brand { left: 29px; top: 27px; }
  .card--front .brand__name { color: var(--ink); }
  .card--back .brand { left: 27px; top: 170px; }
  .card--back .brand__name { color: #ffffff; }

  .person {
    position: absolute;
    left: 29px;
    top: 155px;
    width: 371px;
  }
  .person__row { display: flex; align-items: flex-end; gap: 6px; }
  .person__name {
    font-weight: 700;
    font-size: 13.5px;
    color: var(--ink);
    line-height: 1;
    white-space: nowrap;
  }
  .person__rule {
    flex: 1;
    height: 1px;
    background: var(--ink-soft);
    margin-bottom: 1px;
  }
  .person__role {
    margin-top: 3px;
    font-size: 11.5px;
    color: var(--brand-red);
  }

  .contact {
    position: absolute;
    right: 29px;
    top: 176px;
    list-style: none;
  }
  .contact__item {
    display: flex;
    justify-content: flex-end;
    align-items: center;
    gap: 5px;
    height: 15px;
    font-size: 10.5px;
    color: var(--ink);
  }
  .contact__icon { width: 9px; height: 9px; fill: var(--brand-red); }
</style>
</head>
<body>
<main class="sheet">

  <section class="card card--front" aria-label="Business card front">
    <div class="card__ring"></div>
    <div class="brand">
      <span class="brand__dot"></span>
      <span class="brand__name">Steadfast MD</span>
    </div>
    <div class="person">
      <div class="person__row">
        <span class="person__name">Daniel Hart</span>
        <span class="person__rule"></span>
      </div>
      <p class="person__role">Managing Director</p>
    </div>
    <ul class="contact">
      <li class="contact__item">214-555-0148
        <svg class="contact__icon" viewBox="0 0 10 10"><path d="M2 0.5 L3.6 2.6 L2.7 3.6 Q3.6 5.6 6.4 7.3 L7.4 6.4 L9.5 8 L8.3 9.5 Q4.5 9.2 0.5 1.7 Z"/></svg>
      </li>
      <li class="contact__item">daniel@steadfastmd.com
        <svg class="contact__icon" viewBox="0 0 10 10"><path d="M0.5 2 H9.5 V8 H0.5 Z M1.3 2.6 L5 5.4 L8.7 2.6 Z" fill-rule="evenodd"/></svg>
      </li>
      <li class="contact__item">www.steadfastmd.com
        <svg class="contact__icon" viewBox="0 0 10 10"><circle cx="5" cy="5" r="4.3" fill="none" stroke="#e3231b" stroke-width="1"/><path d="M0.8 5 H9.2 M5 0.8 V9.2" stroke="#e3231b" stroke-width="0.8"/><ellipse cx="5" cy="5" rx="2" ry="4.3" fill="none" stroke="#e3231b" stroke-width="0.8"/></svg>
      </li>
    </ul>
  </section>

  <section class="card card--back" aria-label="Business card back">
    <div class="card__ring"></div>
    <div class="brand">
      <span class="brand__dot"></span>
      <span class="brand__name">Steadfast MD</span>
    </div>
  </section>

</main>
</body>
</html>
```